Brindle Outcomes WebDesign

Although the designs we have had are great we are looking for something unique and would like to move away from the traditional. We append additional comments and files to reflect this. WE are looking for designs to showcase there artistic flare.

Task
To design Brindle Outcomes home page and a second page ie information on our Internet Marketing Services

Client:
Brindle Outcomes is the next generation provider of international marketing, branding, design, Search Engine Optimization(SEO) and Search Engine Marketing(SEM). Utilising a variety of crowd-source channels and trust networks, Brindle Outcomes is able to offer you a complete internet marketing package. From initial design and branding to the continued work on SEO all our services are geared towards dramatically increasings your revenues. Our primary goal is to build greater trading bridges between English-speaking and Chinese-speaking worlds. We believe that a true understanding of the local market is only achievable if you are a native speaker. The power of our networks and processes have been focused to enable Brindle Outcomes to enlist only native speakers to bolster your Internet Marketing Campaign.

The primary color pallet is:

FF9571
B23308
FF6633
858585
BDBDBD
or
https://palettes.vormix.example/#themes/search?term=brindle%20outcomes

Sites we like
http://www.trevonix.example/
http://www.morbela.example/
Updates

We have believe that we will need to push our design packages (outsourced through artflockly) more. We would like this to be reflected on the front page.

This means that the menu should also include

Design
Also the use of content management system wendix

Have added a few more sites that we like
www.harbourpixelstudio.example.hk
www.qmt.example.hk

Really excited with all the designs so far.  We would like the design to move away from the more standard layout. With this in mind we would like to see some design that feature hexagons, or decagons.
Please feel free to let loose! we want a design that is quit unique

We have included to vector files.

vector file 8016151 is for a color reference we thik that in order to enhence the design we need to expand the color palette, would want to maintain the primary corporate colors, but include some bright additional colors.

The second was our insipration for the the hexagon. expanding on the idea we thought that the main menu could be made up of hexagons. The ad/info modules that appear half way up the page be similar to those in the vector.

Reason: Have updated brief and are looking for a more unique feel to the design.

Target Market(s)

Small to medium business looking to branch out further in the international market

Industry/Entity Type

Internet

Requirements
Must have
• A login/search section
A separate floating feedback tab
Main Navigation – Home, Internet Marketing, Cloud Computing
A banner space from informative text on our services
Must have a request for a quote on each page

```html
<!DOCTYPE html>
<html lang="en">
<head>
<meta charset="utf-8">
<title>Brindle Outcomes — SEO and Cloud Consultant</title>
<link rel="stylesheet" href="https://fonts.googleapis.com/css2?family=Source+Sans+3:wght@300;400;600;700&display=swap">
<style>
:root{
  --orange:#ff6633;
  --orange-deep:#e8481a;
  --orange-dark:#b23308;
  --peach:#ff9571;
  --amber:#f6a300;
  --violet:#7b2fd0;
  --crimson:#b2112b;
  --gray:#858585;
  --gray-light:#bdbdbd;
  --ink:#4a4a4a;
  --ink-soft:#6b6b6b;
  --paper:#ffffff;
  --band:#f3f3f3;
  --slate:#4c5158;
}
*{box-sizing:border-box;margin:0;padding:0}
html,body{width:1200px;height:2290px;overflow:hidden}
body{position:relative;background:var(--paper);font-family:"Source Sans 3",Arial,sans-serif;color:var(--ink)}
.abs{position:absolute}

/* header */
.top-rule{left:0;top:0;width:1200px;height:6px;background:#e4e4e4}
.brand-mark{left:69px;top:43px;width:76px;height:76px;border-radius:50%;background:var(--orange-deep)}
.brand-name{left:171px;top:48px;font-size:36px;font-weight:600;color:var(--gray);letter-spacing:-.5px;white-space:nowrap}
.brand-tag{left:208px;top:92px;font-size:13px;font-weight:600;color:#222}
.login-field{top:26px;height:24px;border-radius:4px;background:#e3e3e3;font-size:12px;color:#666;padding:4px 10px}
.login-user{left:792px;width:133px}
.login-pass{left:931px;width:133px}
.login-btn{left:1069px;top:26px;width:69px;height:24px;border-radius:4px;background:#6b6b6b;color:#fff;font-size:13px;text-align:center;line-height:24px}
.main-nav{top:100px;left:701px;display:flex;font-size:19px;color:#555}
.main-nav a{color:inherit;text-decoration:none;padding:0 14px;border-left:1px solid #ccc;line-height:26px}
.main-nav a:first-child{padding-left:0;border-left:0}

/* hero */
.hero{left:0;top:145px;width:1200px;height:574px;background:linear-gradient(180deg,#ff6a35 0%,#f1541f 55%,#c93a0e 100%)}
.hero-title{left:0;top:40px;width:1200px;text-align:center;font-size:42px;font-weight:300;color:#fff}
.hero-sub{left:0;top:103px;width:1200px;text-align:center;font-size:16px;color:#ffd9c8}
.hero-art{left:0;top:0}

/* service columns */
.col-title{top:754px;font-size:23px;color:var(--orange-dark)}
.col-pic{top:794px;width:341px;height:151px}
.col-head{top:958px;font-size:15px;color:#333;width:341px}
.col-body{top:982px;width:337px;font-size:12.5px;line-height:20px;color:#555;text-align:justify}
.pic-seo{background:linear-gradient(135deg,#f4f4f4,#d9d9d9 60%,#8f8f8f)}
.pic-cloud{background:linear-gradient(180deg,#f6f6f6,#e3e3e3 60%,#4f9a4a 85%,#2f6fb5)}
.pic-market{background:linear-gradient(135deg,#eef1f4,#cfd5dc 55%,#f3f3f3)}
.divider{left:61px;top:1070px;width:1078px;height:1px;background:#dcdcdc}

/* services */
.svc-title{left:63px;top:1093px;font-size:22px;color:var(--orange-dark)}
.svc-text{left:63px;width:693px;font-size:14px;line-height:20.6px;color:#555}
.svc-item{left:78px;width:585px;height:93px;border-bottom:1px solid #dedede}
.svc-item.is-active{background:#f1f1f1;border-bottom:0}
.svc-icon{position:absolute;left:17px;top:14px;width:64px;height:64px;border-radius:50%;background:var(--slate)}
.is-active .svc-icon{background:var(--crimson)}
.svc-icon svg{position:absolute;left:16px;top:16px}
.svc-item h4{position:absolute;left:107px;top:14px;font-size:15px;font-weight:400;color:#333}
.svc-item p{position:absolute;left:107px;top:38px;width:440px;font-size:12px;line-height:20px;color:#666}

/* quote form */
.quote-panel{left:800px;top:1090px;width:341px;height:526px;border-radius:6px;background:linear-gradient(180deg,#f8f8f8,#ececec);box-shadow:0 1px 3px rgba(0,0,0,.15)}
.quote-ribbon{left:786px;top:1110px}
.quote-ribbon span{position:absolute;left:34px;top:10px;font-size:21px;color:#fff;white-space:nowrap}
.q-label{left:821px;font-size:13px;color:#555}
.q-input{left:821px;width:295px;height:31px;border:1px solid #d4d4d4;border-radius:3px;background:#fff}
.q-submit{left:825px;top:1558px;width:111px;height:32px;border-radius:3px;background:linear-gradient(180deg,#f0602c,#c8380c);color:#fff;font-size:13px;font-weight:600;text-align:center;line-height:32px}

/* projects */
.projects{left:0;top:1646px;width:1200px;height:334px;background:var(--band);border-top:1px solid #e2e2e2}
.proj-title{left:73px;top:1668px;font-size:27px;color:#333}
.proj-sub{left:73px;top:1705px;font-size:14.5px;color:#555}
.proj-art{left:0;top:1730px}
.back-top{left:1032px;top:1953px;font-size:13px;color:#fff;display:flex;align-items:center;gap:8px}

/* footer */
.footer{left:0;top:1980px;width:1200px;height:260px;background:linear-gradient(180deg,#f56630,#e14f1b)}
.foot-mark{left:75px;top:2031px;width:61px;height:61px;border-radius:50%;background:#fff}
.foot-name{left:150px;top:2045px;font-size:30px;font-weight:600;color:#fff;white-space:nowrap}
.call-label{left:78px;top:2112px;font-size:14px;color:#ffc7ad}
.call-num{left:172px;top:2105px;font-size:26px;color:#fff}
.social{top:2154px;width:26px;height:26px;border-radius:50%;background:#fff}
.foot-rule{top:2028px;width:1px;height:159px;background:rgba(255,255,255,.35)}
.foot-head{top:2020px;font-size:20px;color:#fff;display:flex;align-items:center;gap:8px}
.foot-head i{display:inline-block;width:14px;height:14px;border-radius:50%;background:#fff}
.tweet{left:455px;width:290px;font-size:12.5px;line-height:20px;color:#fff}
.tweet b{font-weight:700}
.testimonial{left:814px;top:2060px;width:300px;font-size:12.5px;line-height:20px;color:#fff;font-style:italic}
.quote-mark{font-size:32px;color:#fff;font-style:normal;line-height:1}
.author{left:814px;top:2174px;font-size:13px;font-weight:700;color:#fff}
.bottom-bar{left:0;top:2240px;width:1200px;height:50px;background:#c33a10;font-size:12px;color:#ffd2bf}
.bottom-bar .copy{position:absolute;left:73px;top:17px}
.bottom-bar .links{position:absolute;right:80px;top:17px;word-spacing:2px}
</style>
</head>
<body>

<!-- header -->
<div class="abs top-rule"></div>
<div class="abs brand-mark"></div>
<div class="abs brand-name">BrindleOutcomes.com</div>
<div class="abs brand-tag">SEO and Cloud Consultant</div>
<div class="abs login-field login-user">username</div>
<div class="abs login-field login-pass">password</div>
<div class="abs login-btn">Log In</div>
<nav class="abs main-nav"><a href="#">Home</a><a href="#">Internet Marketing</a><a href="#">Cloud Computing</a></nav>

<!-- hero -->
<section class="abs hero">
  <svg class="abs hero-art" width="1200" height="574" viewBox="0 0 1200 574">
    <!-- left hexagon -->
    <polygon points="230,132 374,215 374,380 230,463 86,380 86,215" fill="#c9380e"/>
    <polygon points="238,142 378,224 374,384 232,458 96,378 100,220" fill="#e0471a"/>
    <polygon points="232,188 338,249 338,372 232,433 126,372 126,249" fill="#fff"/>
    <g role="img" aria-label="Businessman touching a cloud on a virtual screen">
      <polygon points="232,200 327,255 327,366 232,421 137,366 137,255" fill="url(#skyA)"/>
    </g>
    <!-- middle hexagon -->
    <polygon points="598,138 752,240 745,420 590,490 425,410 418,220" fill="#c53b12"/>
    <polygon points="583,128 742,218 742,402 583,494 424,402 424,218" fill="#f0793c"/>
    <polygon points="583,170 705,240 705,382 583,452 461,382 461,240" fill="#fff"/>
    <g role="img" aria-label="Laptop connected to clouds in a blue sky">
      <polygon points="583,182 695,246 695,376 583,440 471,376 471,246" fill="url(#skyB)"/>
    </g>
    <!-- right hexagon -->
    <polygon points="935,155 1092,235 1100,410 955,478 790,420 782,245" fill="#d12e12"/>
    <polygon points="945,160 1105,252 1105,436 945,528 785,436 785,252" fill="var(--amber)"/>
    <polygon points="945,208 1063,276 1063,412 945,480 827,412 827,276" fill="#fff"/>
    <g role="img" aria-label="Man standing on a laptop keyboard facing a city skyline">
      <polygon points="945,220 1053,282 1053,406 945,468 837,406 837,282" fill="url(#skyC)"/>
    </g>
    <!-- slider tab -->
    <polygon points="534,574 556,533 658,533 680,574" fill="#b8350c"/>
    <circle cx="580" cy="557" r="5" fill="#fff"/><circle cx="597" cy="557" r="5" fill="#fff"/>
    <circle cx="615" cy="557" r="5" fill="#fff"/><circle cx="634" cy="557" r="5" fill="#fff"/>
    <defs>
      <linearGradient id="skyA" x1="0" y1="0" x2="0" y2="1"><stop offset="0" stop-color="#2f6fd0"/><stop offset=".55" stop-color="#8fc0ee"/><stop offset="1" stop-color="#3a6aa8"/></linearGradient>
      <linearGradient id="skyB" x1="0" y1="0" x2="0" y2="1"><stop offset="0" stop-color="#2a78d6"/><stop offset=".5" stop-color="#cfe6fb"/><stop offset="1" stop-color="#3c8fd8"/></linearGradient>
      <linearGradient id="skyC" x1="0" y1="0" x2="0" y2="1"><stop offset="0" stop-color="#4c8fd6"/><stop offset=".55" stop-color="#c9dcee"/><stop offset="1" stop-color="#6f7780"/></linearGradient>
    </defs>
  </svg>
  <h1 class="abs hero-title">Web Provide SEO &amp; Clouds Consultancy..</h1>
  <p class="abs hero-sub">Pellentesque habitant morbi tristique senectus et netus et malesuada fames ac turpis egestas.</p>
</section>

<!-- service columns -->
<h2 class="abs col-title" style="left:61px;font-weight:400">SEO Service</h2>
<h2 class="abs col-title" style="left:429px;font-weight:400">Clouds Computing</h2>
<h2 class="abs col-title" style="left:799px;font-weight:400">Internet Marketing</h2>
<div class="abs col-pic pic-seo" style="left:61px" role="img" aria-label="Pen sketching an SEO diagram on paper"></div>
<div class="abs col-pic pic-cloud" style="left:429px" role="img" aria-label="Globe with cloud service icons arcing above"></div>
<div class="abs col-pic pic-market" style="left:799px" role="img" aria-label="Tablet showing a chart beside a coffee cup and reports"></div>
<h3 class="abs col-head" style="left:64px;font-weight:400">Mauris vel lacus vitae felis</h3>
<h3 class="abs col-head" style="left:436px;font-weight:400">Mauris vel lacus vitae felis</h3>
<h3 class="abs col-head" style="left:804px;font-weight:400">Mauris vel lacus vitae felis</h3>
<p class="abs col-body" style="left:64px">Cum sociis natoque penatibus et magnis dis parturient montes, nascetur ridiculus mus. In iaculis facilisis</p>
<p class="abs col-body" style="left:436px">Cum sociis natoque penatibus et magnis dis parturient montes, nascetur ridiculus mus. In iaculis facilisis massa.</p>
<p class="abs col-body" style="left:804px">Cum sociis natoque penatibus et magnis dis parturient montes, nascetur ridiculus mus. In iaculis facilisis massa.</p>
<div class="abs divider"></div>

<!-- services we provide -->
<h2 class="abs svc-title" style="font-weight:400">Services We Provide</h2>
<p class="abs svc-text" style="top:1128px">Lorem ipsum dolor sit amet, consectetuer adipiscing elit. Nam cursus. Morbi ut mi. Nullam enim leo, egestas id, condimentum at, laoreet mattis, massa.</p>
<p class="abs svc-text" style="top:1186px">Sed eleifend nonummy diam. Praesent mauris ante, elementum et, bibendum at, posuere sit amet, nibh. Duis tincidunt lectus quis dui viverra vestibulum. Suspendisse vulputate aliquam dui. Nulla elementum dui ut augue. Aliquam vehicula mi at mauris. Maecenas placerat, nisl at consequat rhoncus, sem nunc gravida justo, quis eleifend arcu velit quis lacus. Morbi magna magna, tincidunt a, mattis non, imperdiet vitae, tellus. Sed odio est, auctor ac, sollicitudin in, consequat vitae, orci. Fusce id felis. Vivamus sollicitudin metus eget eros.</p>

<div class="abs svc-item is-active" style="top:1327px">
  <div class="svc-icon"><svg width="32" height="32" viewBox="0 0 32 32"><rect x="3" y="5" width="26" height="17" rx="2" fill="none" stroke="#fff" stroke-width="3"/><rect x="13" y="22" width="6" height="4" fill="#fff"/><rect x="9" y="26" width="14" height="3" fill="#fff"/></svg></div>
  <h4>Cras id elit. Integer quis urna.</h4>
  <p>Mauris vel lacus vitae felis vestibulum volutpat. Etiam est nunc, venenatis in, tristique eu, imperdiet ac, nisl. Cum sociis natoque penatibus et magnis d</p>
</div>
<div class="abs svc-item" style="top:1423px">
  <div class="svc-icon"><svg width="32" height="32" viewBox="0 0 32 32"><circle cx="16" cy="16" r="10" fill="none" stroke="#fff" stroke-width="6" stroke-dasharray="4 3.85"/><circle cx="16" cy="16" r="8" fill="#fff"/><circle cx="16" cy="16" r="3.5" fill="var(--slate)"/></svg></div>
  <h4>Cras id elit. Integer quis urna.</h4>
  <p>Mauris vel lacus vitae felis vestibulum volutpat. Etiam est nunc, venenatis in, tristique eu, imperdiet ac, nisl. Cum sociis natoque penatibus et magnis d</p>
</div>
<div class="abs svc-item" style="top:1519px;border-bottom:0">
  <div class="svc-icon"><svg width="32" height="32" viewBox="0 0 32 32"><ellipse cx="16" cy="14" rx="12" ry="9" fill="none" stroke="#fff" stroke-width="3"/><path d="M9 21 L7 28 L14 22.5" fill="#fff"/></svg></div>
  <h4>Cras id elit. Integer quis urna.</h4>
  <p>Mauris vel lacus vitae felis vestibulum volutpat. Etiam est nunc, venenatis in, tristique eu, imperdiet ac, nisl. Cum sociis natoque penatibus et magnis d</p>
</div>

<!-- request a quote -->
<aside class="abs quote-panel"></aside>
<div class="abs quote-ribbon">
  <svg width="324" height="58" viewBox="0 0 324 58"><polygon points="0,0 302,0 324,46 14,46" fill="#3f3f3f"/><polygon points="0,46 14,46 14,58" fill="#222"/></svg>
  <span>Request a Quote</span>
</div>
<label class="abs q-label" style="top:1187px">Full Name:</label>
<div class="abs q-input" style="top:1206px"></div>
<label class="abs q-label" style="top:1246px">Email address:</label>
<div class="abs q-input" style="top:1266px"></div>
<label class="abs q-label" style="top:1307px">Phone no:</label>
<div class="abs q-input" style="top:1328px"></div>
<label class="abs q-label" style="top:1370px">Website:</label>
<div class="abs q-input" style="top:1391px"></div>
<label class="abs q-label" style="top:1432px">Message</label>
<div class="abs q-input" style="top:1454px;height:93px"></div>
<div class="abs q-submit">Submit Now</div>

<!-- working projects -->
<section class="abs projects"></section>
<h2 class="abs proj-title" style="font-weight:400">Working Projects</h2>
<p class="abs proj-sub">Curabitur vel dolor ultrices ipsum dictum tristique. Praesent vitae lacus. Ut velit enim, vestibulum non.</p>
<svg class="abs proj-art" width="1200" height="250" viewBox="0 0 1200 250">
  <!-- pair one -->
  <polygon points="90,26 180,26 226,112 180,198 90,198 44,112" fill="#f2a51a"/>
  <polygon points="100,44 172,44 208,112 172,180 100,180 64,112" fill="url(#shotA)" role="img" aria-label="Technology website preview"/>
  <polygon points="258,40 352,40 400,128 352,216 258,216 210,128" fill="#ee7a14"/>
  <polygon points="266,58 344,58 382,128 344,198 266,198 228,128" fill="url(#shotB)" role="img" aria-label="Website preview with robot character"/>
  <!-- pair two -->
  <polygon points="470,26 560,26 606,112 560,198 470,198 424,112" fill="#8a36d8"/>
  <polygon points="480,44 552,44 588,112 552,180 480,180 444,112" fill="url(#shotC)" role="img" aria-label="Web development agency preview"/>
  <polygon points="634,36 728,36 776,124 728,212 634,212 586,124" fill="var(--violet)"/>
  <polygon points="642,54 720,54 758,124 720,194 642,194 604,124" fill="url(#shotD)" role="img" aria-label="Advertising site preview with chart"/>
  <!-- pair three -->
  <polygon points="850,26 940,26 986,112 940,198 850,198 804,112" fill="#e0502a"/>
  <polygon points="860,44 932,44 968,112 932,180 860,180 824,112" fill="url(#shotE)" role="img" aria-label="Holiday themed website preview"/>
  <polygon points="1012,36 1102,36 1148,124 1102,212 1012,212 966,124" fill="#d2301a"/>
  <polygon points="1020,54 1094,54 1130,124 1094,194 1020,194 984,124" fill="url(#shotF)" role="img" aria-label="Holiday website preview with decorated tree"/>
  <!-- band edge -->
  <polygon points="600,250 1200,216 1200,250" fill="#c8380e"/>
  <defs>
    <linearGradient id="shotA" x1="0" y1="0" x2="0" y2="1"><stop offset="0" stop-color="#2a3a5c"/><stop offset="1" stop-color="#c9ccd3"/></linearGradient>
    <linearGradient id="shotB" x1="0" y1="0" x2="1" y2="1"><stop offset="0" stop-color="#3d5c86"/><stop offset="1" stop-color="#d3d7de"/></linearGradient>
    <linearGradient id="shotC" x1="0" y1="0" x2="0" y2="1"><stop offset="0" stop-color="#c2232a"/><stop offset=".3" stop-color="#e9e35a"/><stop offset="1" stop-color="#9fb93a"/></linearGradient>
    <linearGradient id="shotD" x1="0" y1="0" x2="0" y2="1"><stop offset="0" stop-color="#e6e96a"/><stop offset="1" stop-color="#c7d24a"/></linearGradient>
    <linearGradient id="shotE" x1="0" y1="0" x2="0" y2="1"><stop offset="0" stop-color="#b51f1f"/><stop offset=".45" stop-color="#f2f2f2"/><stop offset="1" stop-color="#e8e8e8"/></linearGradient>
    <linearGradient id="shotF" x1="0" y1="0" x2="0" y2="1"><stop offset="0" stop-color="#c2221f"/><stop offset=".6" stop-color="#2f7a36"/><stop offset="1" stop-color="#7a1c18"/></linearGradient>
  </defs>
</svg>
<div class="abs back-top">Back to top
  <svg width="20" height="20" viewBox="0 0 20 20"><circle cx="10" cy="10" r="8.5" fill="none" stroke="#fff" stroke-width="1.6"/><path d="M10 14 V6 M6.5 9.5 L10 6 L13.5 9.5" fill="none" stroke="#fff" stroke-width="1.6"/></svg>
</div>

<!-- footer -->
<footer class="abs footer"></footer>
<div class="abs foot-mark"></div>
<div class="abs foot-name">BrindleOutcomes.com</div>
<div class="abs call-label">Call Us Today</div>
<div class="abs call-num">+555.010.0147</div>
<span class="abs social" style="left:79px"></span>
<span class="abs social" style="left:111px"></span>
<span class="abs social" style="left:143px"></span>
<span class="abs social" style="left:175px"></span>
<div class="abs foot-rule" style="left:426px"></div>
<div class="abs foot-rule" style="left:768px"></div>

<h3 class="abs foot-head" style="left:455px;font-weight:400">Chirpline Feed</h3>
<p class="abs tweet" style="top:2060px"><b>Mauris vel @</b> lacus vitae felis vestibulum volutpat. Etiam est nunc, venenatis in, tristique</p>
<p class="abs tweet" style="top:2121px"><b>John vel @</b> Sed metus augue, convallis et, vehicula ut, pulvinar eu, ante. Integer orci tellus, tristique vitae, consequat nec, porta vel, lectus.</p>

<h3 class="abs foot-head" style="left:788px;font-weight:400">Testimonial <i></i></h3>
<span class="abs quote-mark" style="left:786px;top:2062px">&ldquo;</span>
<p class="abs testimonial">Nunc tempus felis vitae urna. Vivamus porttitor, neque at volutpat rutrum, purus nisi eleifend libero, a tempus libero lectus feugiat felis. Morbi diam mauris, viverra in, gravida eu, mattis in, ante. Morbi eget arcu. Morbi porta, libero id ullamcorper nonummy</p>
<span class="abs quote-mark" style="left:1030px;top:2142px">&rdquo;</span>
<div class="abs author">by Author Name</div>

<div class="abs bottom-bar">
  <span class="copy">© 2012 Company Name.  All right reserved</span>
  <span class="links">Home &nbsp; / &nbsp; Internet Marketing &nbsp; / &nbsp; Cloud Computing</span>
</div>

</body>
</html>
```